Business Card Design for Small Electrical Contractor

I need to update my business card into something a little more modern. We are a small electrical contracting company. We service domestic and commercial places around Sydney. We have 2 logo designs at the moment. I have uploaded both and 2 different sizes to work with.

Industry/Entity Type

Business

Contact Information for Business Card

Leo Hartigan
8/21-23 Birch Rd, Kelsworth 2087
t - (02) 9381 4720
m - 0427 815 903
E - info@hartiganelx.com.au
W - hartiganelx.com.au
ABN: 42 907 551 316

Font styles to use
Sans Serif

Requirements
Must have
• I would also like to see the below fit on somewhere aswell
• - Licensed Electrician
• - Level 2 (Cat 1 & 4)
• - Domestic
• - Commercial
• - Repairs and Installations
• - Data
Nice to have
• Try and keep similar colours as logo
Should not have
• No lightning bolts or light globes. Smart and professional please.

```html
<!DOCTYPE html>
<html lang="en">
<head>
<meta charset="utf-8">
<title>Hartigan Electrical — Business Card</title>
<link rel="stylesheet" href="https://fonts.googleapis.com/css2?family=Arimo:wght@400;700&display=swap">
<style>
  :root {
    --backdrop: #e9e6e1;
    --card-black: #0b0b0b;
    --card-white: #ffffff;
    --orange: #f39a1e;
    --ink: #1d2b2a;
    --grey: #4a4a4a;
    --rule: #2a3a38;
  }
  * { box-sizing: border-box; margin: 0; padding: 0; }
  html, body {
    width: 1200px; height: 913px; overflow: hidden;
    background: var(--backdrop);
    font-family: "Arimo", Arial, sans-serif;
  }
  .canvas { position: relative; width: 1200px; height: 913px; }

  .card {
    position: absolute;
    width: 560px; height: 342px;
    box-shadow: 0 10px 28px rgba(0,0,0,.22);
  }
  .card--front { left: 80px; top: 90px; background: var(--card-black); }
  .card--back  { left: 560px; top: 480px; background: var(--card-white); }

  .brand { position: absolute; }
  .brand__name {
    font-size: 34px; font-weight: 400; letter-spacing: .5px; line-height: 1;
    white-space: nowrap;
  }
  .brand__rule { height: 2px; background: var(--orange); margin-top: 10px; }

  .card--front .brand { left: 34px; top: 146px; }
  .card--front .brand__name { color: #fff; font-size: 26px; letter-spacing: .3px; }

  .services {
    position: absolute; right: 32px; top: 118px;
    list-style: none; text-align: right;
    color: var(--orange); font-size: 15px; line-height: 26px;
    white-space: nowrap;
  }
  .services .dot { margin: 0 6px; }
  .services li .dot:last-child { margin-right: 0; }

  .card--back .brand { left: 36px; top: 132px; }
  .card--back .brand__name { color: var(--ink); font-size: 30px; }
  .abn { margin-top: 10px; font-size: 14px; color: var(--grey); text-align: right; }
  .abn b { color: var(--orange); }

  .divider {
    position: absolute; left: 322px; top: 62px;
    width: 1px; height: 218px; background: var(--rule);
  }

  .contact { position: absolute; left: 346px; top: 78px; }
  .contact__name {
    color: var(--orange); font-weight: 700; font-size: 19px;
    letter-spacing: .5px; margin-bottom: 12px;
  }
  .contact__list { list-style: none; }
  .contact__item {
    display: flex; align-items: flex-start; gap: 10px;
    font-size: 13.5px; line-height: 18px; color: var(--grey);
    margin-bottom: 6px;
  }
  .contact__item svg { flex: none; width: 14px; height: 14px; margin-top: 2px; fill: var(--orange); }
</style>
</head>
<body>
<main class="canvas">

  <section class="card card--front" aria-label="Card front">
    <div class="brand">
      <div class="brand__name">Hartigan Electrical</div>
      <div class="brand__rule"></div>
    </div>
    <ul class="services">
      <li>Licensed Electrician<span class="dot">•</span></li>
      <li>Level 2 (Cat 1 &amp; 4)<span class="dot">•</span></li>
      <li>Domestic<span class="dot">•</span>Commercial<span class="dot">•</span></li>
      <li>Repairs and Installations<span class="dot">•</span>Data<span class="dot">•</span></li>
    </ul>
  </section>

  <section class="card card--back" aria-label="Card back">
    <div class="brand">
      <div class="brand__name">Hartigan Electrical</div>
      <div class="brand__rule"></div>
      <div class="abn"><b>ABN:</b> 42 907 551 316</div>
    </div>

    <div class="divider"></div>

    <div class="contact">
      <div class="contact__name">LEO HARTIGAN</div>
      <ul class="contact__list">
        <li class="contact__item">
          <svg viewBox="0 0 14 14" aria-hidden="true"><path d="M7 0a5 5 0 0 0-5 5c0 3.6 5 9 5 9s5-5.4 5-9a5 5 0 0 0-5-5zm0 7a2 2 0 1 1 0-4 2 2 0 0 1 0 4z"/></svg>
          <span>8/21-23 Birch Rd<br>Kelsworth 2087</span>
        </li>
        <li class="contact__item">
          <svg viewBox="0 0 14 14" aria-hidden="true"><path d="M1 4c0-1.5 2.5-3 6-3s6 1.5 6 3v1.5h-3V4H4v1.5H1zM3 7h8l1.5 6h-11z"/></svg>
          <span>(02) 9381 4720</span>
        </li>
        <li class="contact__item">
          <svg viewBox="0 0 14 14" aria-hidden="true"><path d="M4 0h6a1 1 0 0 1 1 1v12a1 1 0 0 1-1 1H4a1 1 0 0 1-1-1V1a1 1 0 0 1 1-1zm0 2v9h6V2zm3 9.6a.8.8 0 1 0 0 1.6.8.8 0 0 0 0-1.6z"/></svg>
          <span>0427 815 903</span>
        </li>
        <li class="contact__item">
          <svg viewBox="0 0 14 14" aria-hidden="true"><path d="M1 3h12v8H1zm1 1v.4l5 3.3 5-3.3V4z"/></svg>
          <span>info@hartiganelx.com.au</span>
        </li>
        <li class="contact__item">
          <svg viewBox="0 0 14 14" aria-hidden="true"><path d="M7 0a7 7 0 1 0 0 14A7 7 0 0 0 7 0zm0 1.5a5.5 5.5 0 1 1 0 11 5.5 5.5 0 0 1 0-11zM3 6.3h8v1.4H3z"/></svg>
          <span>www.hartiganelx.com.au</span>
        </li>
      </ul>
    </div>
  </section>

</main>
</body>
</html>
```